BPRV Postcard Design: Mosquito Control, Lawn Maintenance and Pressure washing

I have a new company based in Atlanta,Georgia named Brightwell Pest Relief Ventures, LLC. We specializes in Mosquito Control. We also have additional services: Lawn maintenance, Pressure Washing and Gutter Cleaning. I would like to see designs with the colors Black, Red, Gray. We would like the customer to think of us when it comes to Enjoying a mosquito free yard and improving the look and feel of their home and lawn.

Industry/Entity Type

It Company

Requirements
Nice to have
• Treatment plans starting at $69/mt - front of card
• The additional services we offer - back of card.

```html
<!DOCTYPE html>
<html lang="en">
<head>
<meta charset="utf-8">
<title>BPRV Postcard – Front and Back</title>
<link rel="stylesheet" href="https://fonts.googleapis.com/css2?family=Archivo+Black&family=Oswald:wght@500;700&family=Open+Sans:wght@400;600&family=Dancing+Script:wght@600&display=swap">
<style>
  :root {
    --stage: #3d5577;
    --red-bright: #d3141c;
    --red-deep: #6e0509;
    --black: #0c0c0c;
    --white: #ffffff;
    --silver-light: #f4f4f4;
    --silver-dark: #a9a9a9;
    --ink: #1a1a1a;
    --brand-red: #e0161e;
  }
  * { box-sizing: border-box; margin: 0; padding: 0; }
  html, body { width: 1200px; height: 800px; overflow: hidden; }
  body {
    background: var(--stage);
    font-family: "Open Sans", Arial, sans-serif;
    position: relative;
  }
  .card {
    position: absolute;
    top: 230px;
    width: 540px;
    height: 340px;
    overflow: hidden;
    box-shadow: 0 10px 24px rgba(0,0,0,.35);
    background: var(--black);
  }
  .card--back { left: 40px; }
  .card--front { left: 620px; }

  /* shared brand block */
  .brand { position: absolute; text-align: center; }
  .brand__name {
    font-family: "Archivo Black", Arial, sans-serif;
    color: var(--brand-red);
    font-size: 34px;
    line-height: 1;
    letter-spacing: .5px;
  }
  .brand__sub {
    font-family: "Archivo Black", Arial, sans-serif;
    color: var(--white);
    font-size: 12.5px;
    letter-spacing: .6px;
    margin-top: 3px;
  }
  .brand__phone {
    font-family: "Archivo Black", Arial, sans-serif;
    color: var(--brand-red);
    font-size: 25px;
    letter-spacing: 1.5px;
    margin-top: 4px;
  }

  /* front */
  .front__hero {
    position: absolute; left: 0; top: 0; width: 540px; height: 200px;
    background: radial-gradient(ellipse at 60% 35%, var(--red-bright) 0%, #a10b11 45%, var(--red-deep) 100%);
  }
  .front__banner { position: absolute; left: 230px; top: 22px; width: 300px; height: 96px; }
  .front__banner-text { position: absolute; left: 245px; top: 26px; width: 250px; text-align: center; color: var(--ink); }
  .front__kicker { font-size: 8.5px; font-weight: 600; }
  .front__headline {
    font-family: "Oswald", Arial, sans-serif; font-weight: 700;
    font-size: 31px; line-height: 1; text-transform: uppercase; margin-top: 3px;
  }
  .front__tagline {
    position: absolute; left: 18px; top: 126px; width: 200px; text-align: right;
    font-family: "Oswald", Arial, sans-serif; font-weight: 500; color: var(--white);
    font-size: 23px; line-height: 1.15;
  }
  .front__divider { position: absolute; width: 1px; background: rgba(255,255,255,.7); top: 128px; height: 112px; }
  .front__divider--a { left: 232px; }
  .front__divider--b { left: 362px; }
  .front__price { position: absolute; left: 240px; top: 130px; width: 116px; text-align: center; color: var(--white); }
  .front__price-amount { font-family: "Oswald", Arial, sans-serif; font-weight: 700; font-size: 56px; line-height: 1; }
  .front__price-note { font-size: 8px; letter-spacing: .4px; text-transform: uppercase; margin-top: 2px; }
  .front__copy {
    position: absolute; left: 372px; top: 138px; width: 156px;
    color: var(--white); font-size: 10px; line-height: 1.45;
  }
  .card--front .brand { left: 20px; top: 214px; width: 330px; }

  /* back */
  .back__band { position: absolute; left: 0; top: 0; width: 540px; height: 118px; background: var(--black); }
  .card--back .brand { left: 0; top: 14px; width: 330px; }
  .back__panel {
    position: absolute; left: 0; top: 118px; width: 330px; height: 222px;
    background: radial-gradient(ellipse at 45% 40%, var(--red-bright) 0%, #a10b11 50%, var(--red-deep) 100%);
    color: var(--white); padding: 16px 20px 0 22px;
  }
  .back__mail { position: absolute; left: 330px; top: 118px; width: 210px; height: 222px; background: var(--white); }
  .back__intro { font-size: 12px; line-height: 1.35; }
  .back__services { list-style: none; margin: 8px 0 0 34px; font-size: 12px; line-height: 1.5; }
  .back__services li { display: flex; align-items: center; gap: 8px; }
  .back__services svg { width: 9px; height: 9px; flex: none; }
  .back__cta { font-family: "Dancing Script", cursive; font-size: 17px; margin-top: 10px; }
  .back__address { font-size: 9.5px; margin-top: 10px; padding-left: 18px; }
</style>
</head>
<body>

<section class="card card--back" aria-label="Postcard back">
  <div class="back__band"></div>
  <div class="brand">
    <div class="brand__name">Brightwell</div>
    <div class="brand__sub">Pest Relief Ventures, LLC</div>
    <div class="brand__phone">770-555-0148</div>
  </div>
  <div class="back__panel">
    <p class="back__intro">In addition to Mosquito Control, we also offer these services:</p>
    <ul class="back__services">
      <li><svg viewBox="0 0 10 10"><path d="M1 5h7M5 2l3 3-3 3" stroke="#fff" stroke-width="1.6" fill="none"/></svg>Lawn Maintenance</li>
      <li><svg viewBox="0 0 10 10"><path d="M1 5h7M5 2l3 3-3 3" stroke="#fff" stroke-width="1.6" fill="none"/></svg>Pressure Washing</li>
      <li><svg viewBox="0 0 10 10"><path d="M1 5h7M5 2l3 3-3 3" stroke="#fff" stroke-width="1.6" fill="none"/></svg>Gutter Cleaning</li>
    </ul>
    <p class="back__cta">Call us today to see what we can do for you!</p>
    <p class="back__address">1450 Cedar Hollow Rd SE, Marlow, GA 30099</p>
  </div>
  <div class="back__mail"></div>
</section>

<section class="card card--front" aria-label="Postcard front">
  <div class="front__hero"></div>
  <svg class="front__banner" viewBox="0 0 300 96" aria-hidden="true">
    <defs>
      <linearGradient id="silver" x1="0" y1="0" x2="0" y2="1">
        <stop offset="0" stop-color="var(--silver-light)"/>
        <stop offset=".55" stop-color="#dcdcdc"/>
        <stop offset="1" stop-color="var(--silver-dark)"/>
      </linearGradient>
    </defs>
    <polygon points="0,0 262,0 300,48 262,96 0,96" fill="url(#silver)"/>
  </svg>
  <div class="front__banner-text">
    <p class="front__kicker">Brightwell Pest Relief Ventures Dedicated to</p>
    <h1 class="front__headline">Controlling<br>Mosquitos!</h1>
  </div>
  <p class="front__tagline">Enjoy A Mosquito<br>Free Yard</p>
  <span class="front__divider front__divider--a"></span>
  <div class="front__price">
    <div class="front__price-amount">$69</div>
    <div class="front__price-note">Per month special</div>
  </div>
  <span class="front__divider front__divider--b"></span>
  <p class="front__copy">We are dedicated to controlling those pesky little mosquitos while helping you maintain your lawn and home. Call us today to find out about our great monthly specials.</p>
  <div class="brand">
    <div class="brand__name">Brightwell</div>
    <div class="brand__sub">Pest Relief Ventures, LLC</div>
    <div class="brand__phone">770-555-0148</div>
  </div>
</section>

</body>
</html>
```